Business Card Design Project

KV Strategy Partners is a management consulting business with C-suite (CEO/CFO etc) target clients. Logo selected is blue with simple/serious typefaces.

Target Market(s)

CEOs and CFOs of large corporates

Industry/Entity Type

Management Consulting

Font styles to use
Serif

Colors
3276b5

Requirements
Must have
• Tag line: Building successful collaborations (use different font)
Address: 457 Cedar Brook Lane #03-22 Singapore 519307
Telephone: +65 8372 6094
Email: kvlorne@mailbox47.com

```html
<!DOCTYPE html>
<html lang="en">
<head>
<meta charset="utf-8">
<title>KV Strategy Partners – Business Card</title>
<link rel="stylesheet" href="https://fonts.googleapis.com/css2?family=Libre+Baskerville:wght@700&family=Cormorant+Garamond:wght@500&family=Lora:wght@500;600&display=swap">
<style>
  :root {
    --canvas: #ffffff;
    --frame-blue: #3276b5;
    --card-grey: #bcbdc0;
    --card-black: #0d0d0d;
    --band-dark: #1e1e1e;
    --brand-blue: #1ea7e1;
    --accent-green: #8dc63f;
    --tagline-navy: #2e2a6b;
    --ink: #151515;
    --rule-grey: #8d8e91;
  }
  html, body {
    margin: 0;
    padding: 0;
    width: 1200px;
    height: 1017px;
    overflow: hidden;
    background: var(--canvas);
  }
  .canvas {
    position: relative;
    width: 1200px;
    height: 1017px;
    box-sizing: border-box;
    border-top: 1px solid var(--frame-blue);
    border-left: 1px solid var(--frame-blue);
  }
  .card {
    position: absolute;
    width: 424px;
    overflow: hidden;
  }
  /* Front */
  .card--front {
    left: 186px;
    top: 375px;
    height: 265px;
    background: var(--card-grey);
  }
  .front__band {
    position: absolute;
    left: 0; top: 0;
    width: 100%;
    height: 155px;
    background: var(--band-dark);
    display: flex;
    align-items: center;
    justify-content: center;
  }
  .brand-name {
    font-family: "Libre Baskerville", "Georgia", serif;
    font-weight: 700;
    font-size: 27px;
    color: var(--brand-blue);
    margin: 0;
  }
  .tagline {
    position: absolute;
    left: 51px;
    top: 184px;
    width: 313px;
    height: 33px;
    box-sizing: border-box;
    border-top: 1.6px solid var(--tagline-navy);
    border-bottom: 1.6px solid var(--tagline-navy);
    display: flex;
    align-items: center;
    justify-content: center;
  }
  .tagline__text {
    font-family: "Cormorant Garamond", "Times New Roman", serif;
    font-weight: 500;
    font-size: 21px;
    color: var(--tagline-navy);
    margin: 0;
    white-space: nowrap;
  }
  /* Back */
  .card--back {
    left: 636px;
    top: 378px;
    height: 263px;
    background: var(--card-grey);
  }
  .contact {
    position: absolute;
    left: 68px;
    top: 79px;
    padding-left: 10px;
    border-left: 3px solid var(--rule-grey);
    font-family: "Lora", "Georgia", serif;
    font-weight: 600;
    font-size: 17px;
    line-height: 25px;
    color: var(--ink);
    margin: 0;
    font-style: normal;
    white-space: nowrap;
  }
  .back__band {
    position: absolute;
    left: 0; bottom: 0;
    width: 100%;
    height: 89px;
    background: var(--card-black);
    display: flex;
    align-items: center;
    justify-content: center;
  }
  .email {
    font-family: "Lora", "Georgia", serif;
    font-weight: 600;
    font-size: 18px;
    color: var(--accent-green);
    margin: 0;
    white-space: nowrap;
  }
</style>
</head>
<body>
<main class="canvas">
  <section class="card card--front" aria-label="Business card front">
    <div class="front__band">
      <p class="brand-name">KV Strategy Partners</p>
    </div>
    <div class="tagline">
      <p class="tagline__text">Building successful collaborations</p>
    </div>
  </section>

  <section class="card card--back" aria-label="Business card back">
    <address class="contact">
      457 Cedar Brook<br>
      Lane #03-22 Singapore 519307<br>
      Telephone: +65 8372 6094
    </address>
    <div class="back__band">
      <p class="email">Email: kvlorne@mailbox47.com</p>
    </div>
  </section>
</main>
</body>
</html>
```